ALPINE Institute for Advancement and Practice in Operations

We need a Christmas card containing the following elements :
- text : " Happy Holidays! We wish good health for 2018.

We also take the opportunity to invite you to the inaugural ceremony of our training centre on the 17th April 2018. Save the date! "

- words/drawings with the following topics :
- surgery
- training
- excellence
- precision (especially Swiss precision)

- touch of humour
- modernity
- our logo
- photo of the centre
- format : A4 folded (landscape orientation)

Target Market(s)

Clients / Surgeons / Delegates / Suppliers

Industry/Entity Type

Training

Font styles to use
Sans Serif

Colors
f04a50
ec1f27
ffffff

Requirements
Must have
• color red (C0, M90, J73, N100)
Should not have
• no shocking images (even if surgical domain)

```html
<!DOCTYPE html>
<html lang="en">
<head>
<meta charset="utf-8">
<title>ALPINE Institute – Holiday Card</title>
<link href="https://fonts.googleapis.com/css2?family=Barlow:wght@300;400;600&display=swap" rel="stylesheet">
<style>
  :root {
    --red: #ec1f27;
    --red-soft: #f04a50;
    --ink: #222222;
    --paper: #ffffff;
    --rule: #9a9a9a;
  }
  * { margin: 0; padding: 0; box-sizing: border-box; }
  html, body { width: 1200px; height: 1200px; overflow: hidden; background: var(--paper); }
  body { font-family: "Barlow", Arial, sans-serif; position: relative; }

  .spread { position: absolute; left: 0; top: 0; width: 1200px; height: 440px; }

  .centre-photo {
    position: absolute; left: 14px; top: 86px; width: 416px; height: 278px;
    background: linear-gradient(180deg, #eef1f3 0%, #f8f9fa 45%, #dcdfe2 70%, #f3f4f5 100%);
  }

  .tagline {
    position: absolute; left: 25px; top: 375px;
    font-size: 10px; font-weight: 400; letter-spacing: 0.2px; color: var(--red);
    text-transform: uppercase; white-space: nowrap;
  }
  .tagline .op { color: var(--ink); margin: 0 2px; }
  .tagline sup { color: var(--ink); font-size: 9px; }

  .footnote-rule { position: absolute; left: 25px; top: 397px; width: 74px; height: 1px; background: var(--rule); }
  .footnote { position: absolute; left: 25px; top: 403px; font-size: 7px; color: var(--red); }

  .brand { position: absolute; display: flex; align-items: center; gap: 8px; }
  .brand-name {
    font-size: 5.5px; line-height: 1.25; font-weight: 400; color: var(--ink);
    text-transform: uppercase; text-align: right; letter-spacing: 0.1px;
  }
  .brand-dot { width: 18px; height: 18px; border-radius: 50%; background: var(--red); flex: none; }
  .brand--cover { right: 620px; top: 58px; }
  .brand--inside { right: 294px; top: 360px; }

  .greeting {
    position: absolute; left: 704px; top: 64px; width: 380px;
    text-align: center; color: var(--red); white-space: nowrap;
    font-size: 22px; font-weight: 300; line-height: 28px; letter-spacing: 0.3px;
  }
  .greeting sup { font-size: 11px; line-height: 0; }
</style>
</head>
<body>
  <section class="spread">
    <div class="centre-photo" role="img" aria-label="Photo of the bright, modern surgical training centre with rows of operating tables and monitors"></div>

    <p class="tagline">Surgery <span class="op">(=)</span> Training <span class="op">(+)</span> Excellence <span class="op">(+)</span> Precision<sup>*</sup></p>
    <div class="footnote-rule"></div>
    <p class="footnote">*especially Swiss precision</p>

    <div class="brand brand--cover">
      <p class="brand-name">ALPINE Institute for Advancement<br>and Practice in Operations</p>
      <span class="brand-dot"></span>
    </div>

    <p class="greeting">
      Happy<br>Holidays!<br>We wish<br>good health<br>for 2018.<br>We also take the opportunity<br>to invite you to the inaugural<br>ceremony of our training centre<br>on the 17<sup>th</sup> April 2018.<br>Save the date!
    </p>

    <div class="brand brand--inside">
      <p class="brand-name">ALPINE Institute for Advancement<br>and Practice in Operations</p>
      <span class="brand-dot"></span>
    </div>
  </section>
</body>
</html>
```